Business card & Stationary (e.g. Letterhead, Folder design, etc) for Financial Education Company
MoneyPathways
Creative Brief
Simple
Calder Pruitt
Founder & CEO
42 Hadley Ct, Closter, NJ 07624
calder@moneypathways.org
moneypathways.org
I would like to see a nice design, but I am leaving it up to you. It could be the company logo or name but with a nice design.

```html
<!DOCTYPE html>
<html lang="en">
<head>
<meta charset="utf-8">
<title>MoneyPathways Business Card</title>
<link href="https://fonts.googleapis.com/css2?family=Montserrat:wght@400;500;600&display=swap" rel="stylesheet">
<style>
  :root {
    --page: #e9efee;
    --card: #5fc1b6;
    --card-deep: #52b3a8;
    --ink: #ffffff;
    --ink-soft: rgba(255,255,255,0.85);
    --shadow: rgba(20,60,56,0.22);
  }
  * { margin: 0; padding: 0; box-sizing: border-box; }
  html, body {
    width: 1200px; height: 799px; overflow: hidden;
    background: var(--page);
    font-family: "Montserrat", sans-serif;
    color: var(--ink);
  }
  .sheet {
    position: relative; width: 1200px; height: 799px;
    display: flex; align-items: center; justify-content: center; gap: 60px;
  }
  .card {
    position: relative; width: 510px; height: 292px;
    border-radius: 18px;
    background: linear-gradient(135deg, var(--card) 0%, var(--card-deep) 100%);
    box-shadow: 0 14px 34px var(--shadow);
    overflow: hidden;
  }
  /* Front */
  .brand {
    position: absolute; left: 50%; top: 50%;
    transform: translate(-50%, -58%);
    display: flex; align-items: center; gap: 14px;
  }
  .brand-dot {
    width: 46px; height: 46px; border-radius: 50%;
    background: var(--ink);
  }
  .brand-name {
    font-size: 38px; font-weight: 500; letter-spacing: -0.5px;
  }
  .front-web {
    position: absolute; left: 30px; bottom: 24px;
    font-size: 11px; font-weight: 400; color: var(--ink-soft);
    display: flex; align-items: center; gap: 7px;
  }
  /* Back */
  .person {
    position: absolute; left: 38px; top: 44px;
    display: flex; align-items: center; gap: 12px;
  }
  .person-badge {
    width: 28px; height: 28px; border-radius: 3px; background: var(--ink);
    display: flex; align-items: center; justify-content: center;
  }
  .person-name { font-size: 19px; font-weight: 600; letter-spacing: 2px; text-transform: uppercase; }
  .person-role { font-size: 10px; font-weight: 400; color: var(--ink-soft); margin-top: 2px; }
  .contacts {
    position: absolute; left: 38px; top: 108px;
    list-style: none; display: flex; flex-direction: column; gap: 11px;
  }
  .contact { display: flex; align-items: center; gap: 12px; font-size: 11px; color: var(--ink-soft); }
  .contact svg { width: 14px; height: 14px; flex: none; }
  .back-web {
    position: absolute; right: 30px; bottom: 24px;
    font-size: 11px; color: var(--ink-soft);
  }
</style>
</head>
<body>
<main class="sheet">
  <section class="card card-front" aria-label="Card front">
    <div class="brand">
      <span class="brand-dot"></span>
      <span class="brand-name">MoneyPathways</span>
    </div>
    <p class="front-web">
      <svg width="11" height="11" viewBox="0 0 12 12" aria-hidden="true"><circle cx="6" cy="6" r="5" fill="none" stroke="#fff" stroke-width="1.2"/><path d="M1 6h10M6 1c2 2 2 8 0 10M6 1c-2 2-2 8 0 10" fill="none" stroke="#fff" stroke-width="0.9"/></svg>
      www.moneypathways.org
    </p>
  </section>

  <section class="card card-back" aria-label="Card back">
    <div class="person">
      <span class="person-badge">
        <svg width="16" height="16" viewBox="0 0 16 16" aria-hidden="true"><circle cx="8" cy="5" r="3.2" fill="#52b3a8"/><path d="M2 15c0-4 2.7-6 6-6s6 2 6 6z" fill="#52b3a8"/></svg>
      </span>
      <div>
        <h1 class="person-name">Calder Pruitt</h1>
        <p class="person-role">Managing Director</p>
      </div>
    </div>
    <ul class="contacts">
      <li class="contact">
        <svg viewBox="0 0 14 14" aria-hidden="true"><path d="M3 1h2.5l1 3-1.6 1.1a7 7 0 0 0 3.9 3.9L10 7.4l3 1V11a2 2 0 0 1-2 2A10 10 0 0 1 1 3a2 2 0 0 1 2-2z" fill="#fff"/></svg>
        (201) 555-0142
      </li>
      <li class="contact">
        <svg viewBox="0 0 14 14" aria-hidden="true"><rect x="1" y="3" width="12" height="8" rx="1" fill="#fff"/><path d="M1.5 3.5 7 8l5.5-4.5" fill="none" stroke="#52b3a8" stroke-width="1.1"/></svg>
        calder@moneypathways.org
      </li>
      <li class="contact">
        <svg viewBox="0 0 14 14" aria-hidden="true"><circle cx="7" cy="7" r="5.5" fill="none" stroke="#fff" stroke-width="1.3"/><path d="M1.5 7h11M7 1.5c2.2 2.2 2.2 8.8 0 11M7 1.5c-2.2 2.2-2.2 8.8 0 11" fill="none" stroke="#fff" stroke-width="0.9"/></svg>
        moneypathways.org
      </li>
      <li class="contact">
        <svg viewBox="0 0 14 14" aria-hidden="true"><path d="M7 13S2.5 8.2 2.5 5.2a4.5 4.5 0 0 1 9 0C11.5 8.2 7 13 7 13z" fill="#fff"/><circle cx="7" cy="5.2" r="1.6" fill="#52b3a8"/></svg>
        42 Hadley Ct, Closter, NJ 07624
      </li>
    </ul>
    <p class="back-web">www.moneypathways.org</p>
  </section>
</main>
</body>
</html>
```